Spectacular Business Card Design for AI SAAS Plattform called Leapvine.ai

Hi Creators
I need an outstanding new Design for my business card.
I run an AI automated Saas Plattform Called Leapvine.ai

Front side:
Logo
Slogan: DIY Business Development & Social Media Management
Data:
Name: Markus Obelwinter - CEO / Founder
email: m.obelwinter@leapvine.ai
mobile: +43 699 82 37 415

Company name:
Leapvine FlexCo

Backside:

What we stand for Slogan:
Vertrauen in KI-Technologie, getragen von menschlicher Vision: Dein Sprung nach vorn!
+ a fancy design what captures our core competencies - AI automisations, Social Media Management, Business development
(dont know if its too much, but AI and social media should be )

pls find attached the logo and the old design

Industry/Entity Type

AI automations for marketing and business development

Contact Information for Business Card

Front side: Logo Slogan: DIY Business Development & Social Media Management Data: Name: Markus Obelwinter - CEO / Founder email: m.obelwinter@leapvine.ai mobile: +43 699 82 37 415 Company name: Leapvine FlexCo Backside: What we stand for Slogan: Vertrauen in KI-Technologie, getragen von menschlicher Vision: Dein Sprung nach vorn!

Font styles to use
Serif
Sans Serif

Requirements
Nice to have
• a fancy design on the backside, a fancy design what captures our core competencies - AI automisations, Social Media Management, Business development

```html
<!DOCTYPE html>
<html lang="de">
<head>
<meta charset="utf-8">
<title>Leapvine – Business Card</title>
<link href="https://fonts.googleapis.com/css2?family=Raleway:wght@500;700&family=Fira+Sans:wght@400&family=Arvo:wght@400&display=swap" rel="stylesheet">
<style>
  :root {
    --teal: #0288a0;
    --orange: #f28c31;
    --white: #ffffff;
    --ink: #2b2b2b;
    --stage: #b7b7b7;
  }
  * { margin: 0; padding: 0; box-sizing: border-box; }
  html, body { width: 1200px; height: 1200px; overflow: hidden; }
  body { background: var(--stage); position: relative; font-family: "Fira Sans", sans-serif; }

  .card { position: absolute; top: 303px; width: 369px; height: 594px; overflow: hidden; text-align: center; }
  .card--back { left: 201px; color: var(--white); }
  .card--front { left: 599px; width: 364px; background: var(--white); }

  .band { position: absolute; left: 0; right: 0; }
  .band--teal { background: var(--teal); }
  .band--orange { background: var(--orange); }
  .band-intro { top: 0; height: 250px; }
  .band-stand { top: 250px; height: 106px; }
  .band-vision { top: 356px; height: 76px; }
  .band-core { top: 432px; height: 162px; }

  .brand { display: flex; align-items: center; justify-content: center; gap: 10px; }
  .brand-name { font-family: "Arvo", serif; font-weight: 400; }
  .brand-square { width: 12px; height: 12px; background: var(--orange); }

  .card--back .brand { position: absolute; top: 48px; left: 0; right: 0; }
  .card--back .brand-name { font-size: 44px; color: var(--white); }

  .tagline { position: absolute; top: 147px; left: 0; right: 0; font-family: "Raleway", sans-serif; font-weight: 500; font-size: 20px; line-height: 26px; text-transform: uppercase; }

  .section-title { font-family: "Raleway", sans-serif; font-weight: 700; font-size: 19px; text-transform: uppercase; }
  .section-text { font-size: 17px; line-height: 25px; }
  .band-stand .section-title { margin-top: 13px; }
  .band-stand .section-text { margin-top: 8px; }
  .band-vision .section-title { margin-top: 12px; }
  .band-vision .section-text { margin-top: 4px; }
  .band-core .section-title { margin-top: 25px; }
  .band-core .section-text { margin-top: 6px; }

  .card--front .brand { position: absolute; top: 445px; top: 150px; left: 0; right: 0; }
  .card--front .brand-name { font-size: 54px; color: var(--teal); }

  .person { position: absolute; top: 368px; left: 0; right: 0; }
  .person-name { font-family: "Raleway", sans-serif; font-weight: 700; font-size: 23px; line-height: 26px; }
  .person-first { color: var(--teal); }
  .person-last { color: var(--orange); }
  .person-role { font-size: 17px; color: var(--ink); line-height: 20px; }
  .divider { width: 51px; height: 1px; background: var(--teal); margin: 13px auto 14px; }
  .contact { font-size: 17px; line-height: 25px; color: var(--ink); }

  .footer-bar { position: absolute; bottom: 0; height: 8px; }
  .footer-bar--teal { left: 0; width: 50%; background: var(--teal); }
  .footer-bar--orange { right: 0; width: 50%; background: var(--orange); }
</style>
</head>
<body>
  <section class="card card--back" aria-label="Rückseite der Visitenkarte">
    <div class="band band--teal band-intro">
      <div class="brand"><span class="brand-name">Leapvine</span><span class="brand-square"></span></div>
      <p class="tagline">DIY Business Development &amp;<br>Social Media Management</p>
    </div>
    <div class="band band--orange band-stand">
      <h2 class="section-title">What we stand for slogan</h2>
      <p class="section-text">Vertrauen in KI-Technologie, getragen<br>von menschlicher</p>
    </div>
    <div class="band band--teal band-vision">
      <h2 class="section-title">Vision</h2>
      <p class="section-text">Dein Sprung nach vorn!</p>
    </div>
    <div class="band band--orange band-core">
      <h2 class="section-title">Our core competencies</h2>
      <p class="section-text">AI automisations<br>Social Media Management<br>Business development</p>
    </div>
  </section>

  <section class="card card--front" aria-label="Vorderseite der Visitenkarte">
    <div class="brand"><span class="brand-name">Leapvine</span><span class="brand-square"></span></div>
    <div class="person">
      <p class="person-name"><span class="person-first">Markus</span> <span class="person-last">Obelwinter</span></p>
      <p class="person-role">CEO / Founder</p>
      <div class="divider"></div>
      <p class="contact">+43 699 82 37 415<br>m.obelwinter@leapvine.ai</p>
    </div>
    <div class="footer-bar footer-bar--teal"></div>
    <div class="footer-bar footer-bar--orange"></div>
  </section>
</body>
</html>
```